Window company needs new banner

Window company that has 3 focuses needs a new banner ad.

We sell window hardware
We make new sashes and windows
We restore old windows

http://www.tlsashandrenewal.com

I would like to create a new banner ad for our home page. The ad would try to capture the 3 sections listed above. I would also say they are listed in importance. Our main focus is hardware for this ad.

our best pictures are on our website.

Our suppliers websites
http://www.brindle.co.uk
http://www.kelphardware.co.uk
https://www.pellowgoods.com

Target Market(s)

Historical buildings
Restoration contractors
window restorers
DIY home owners
custom window and door fabricators- Trades people

Industry/Entity Type

Home And Garden

Font styles to use
Serif

Requirements
Must have
• Show the high level of quality of our hardware and other services

```html
<!DOCTYPE html>
<html lang="en">
<head>
<meta charset="utf-8">
<title>Window Hardware, Sashes and Restoration Banner</title>
<link rel="stylesheet" href="https://fonts.googleapis.com/css2?family=Tinos:wght@400;700&display=swap">
<style>
  :root {
    --ink: #111111;
    --white: #ffffff;
    --panel: #fbfbfb;
    --red: #e0121b;
    --red-deep: #b00a10;
    --red-light: #ff3a3a;
    --tag-border: #6a6a6a;
    --photo-windows-a: #f4f1ea;
    --photo-windows-b: #8a8a6a;
    --photo-windows-c: #3f4a2c;
    --photo-room-a: #e9e3d6;
    --photo-room-b: #c9b79a;
    --photo-room-c: #9a8a78;
  }
  * { margin: 0; padding: 0; box-sizing: border-box; }
  html, body { width: 1200px; height: 647px; overflow: hidden; background: var(--white); }
  .banner {
    position: relative;
    width: 1200px;
    height: 647px;
    overflow: hidden;
    font-family: "Tinos", "Times New Roman", serif;
    color: var(--ink);
    background: var(--white);
  }
  .photo { position: absolute; top: 0; height: 450px; }
  .photo--windows {
    left: 0; width: 530px;
    background: linear-gradient(100deg, var(--photo-windows-a) 0%, #e2ddd0 25%, var(--photo-windows-b) 50%, var(--photo-windows-c) 75%, #d8d4c8 100%);
  }
  .photo--room {
    left: 530px; width: 670px;
    background: linear-gradient(90deg, #f2efe8 0%, var(--photo-room-a) 20%, var(--photo-room-b) 55%, var(--photo-room-a) 80%, var(--photo-room-c) 100%);
  }
  .panel {
    position: absolute; left: 0; top: 320px; width: 1200px; height: 327px;
    filter: drop-shadow(0 -4px 8px rgba(0,0,0,0.35));
  }
  .badge {
    position: absolute; left: 488px; top: 122px; width: 224px; height: 224px;
    filter: drop-shadow(0 3px 5px rgba(0,0,0,0.35));
  }
  .badge__text {
    position: absolute; left: 488px; top: 122px; width: 224px; height: 224px;
    display: flex; flex-direction: column; align-items: center; justify-content: center;
    color: var(--white); text-align: center; font-size: 25px; line-height: 1.22;
  }
  .badge__text strong { font-weight: 700; }
  .services-title {
    position: absolute; left: 0; width: 1200px; top: 372px;
    text-align: center; font-size: 37px; font-weight: 700;
  }
  .tag {
    position: absolute; height: 46px;
    display: flex; align-items: center; justify-content: center;
    font-size: 29px; white-space: nowrap; background: var(--white);
    border: 2px dotted var(--tag-border);
    outline: 1px solid #9a9a9a; outline-offset: -6px;
  }
  .tag--hardware-supply { left: 270px; top: 430px; width: 250px; }
  .tag--sashes          { left: 535px; top: 430px; width: 180px; }
  .tag--windows         { left: 730px; top: 430px; width: 200px; }
  .tag--glazing         { left: 143px; top: 497px; width: 280px; height: 50px; }
  .tag--hardware-restore{ left: 438px; top: 497px; width: 356px; height: 50px; }
  .tag--draft           { left: 809px; top: 497px; width: 247px; height: 50px; }
  .cta {
    position: absolute; left: 442px; top: 563px; width: 318px; height: 66px;
    filter: drop-shadow(0 2px 3px rgba(0,0,0,0.3));
  }
  .cta__label {
    position: absolute; left: 442px; top: 563px; width: 300px; height: 66px;
    display: flex; align-items: center; justify-content: center;
    color: var(--white); font-size: 34px; font-weight: 700; letter-spacing: 0.5px;
  }
</style>
</head>
<body>
<div class="banner">
  <div class="photo photo--windows" role="img" aria-label="Restored white sash windows with brass hardware opening onto a garden"></div>
  <div class="photo photo--room" role="img" aria-label="Interior room sealed with plastic sheeting during restoration work"></div>

  <svg class="panel" viewBox="0 0 1200 327" aria-hidden="true">
    <path d="M0 117 L600 20 L1200 65 L1200 327 L0 327 Z" fill="var(--panel)"/>
  </svg>

  <svg class="badge" viewBox="0 0 224 224" aria-hidden="true">
    <defs>
      <radialGradient id="badgeFill" cx="50%" cy="45%" r="55%">
        <stop offset="0%" stop-color="var(--red-light)"/>
        <stop offset="70%" stop-color="var(--red)"/>
        <stop offset="100%" stop-color="var(--red-deep)"/>
      </radialGradient>
      <polygon id="octagon" points="104,0 73.5,73.5 0,104 -73.5,73.5 -104,0 -73.5,-73.5 0,-104 73.5,-73.5"/>
    </defs>
    <g transform="translate(112 112)" fill="url(#badgeFill)">
      <use href="#octagon"/>
      <use href="#octagon" transform="rotate(11.25)"/>
      <use href="#octagon" transform="rotate(22.5)"/>
      <use href="#octagon" transform="rotate(33.75)"/>
    </g>
  </svg>
  <div class="badge__text">
    <span>Protecting</span>
    <span><strong>YOU</strong> &amp; your</span>
    <strong>property</strong>
  </div>

  <h2 class="services-title">We supply, make &amp; restore</h2>
  <div class="tag tag--hardware-supply">Window Hardware</div>
  <div class="tag tag--sashes">New Sashes</div>
  <div class="tag tag--windows">New Windows</div>
  <div class="tag tag--glazing">Glazing &amp; Painting</div>
  <div class="tag tag--hardware-restore">Hardware Restoration</div>
  <div class="tag tag--draft">Draft Proofing</div>

  <svg class="cta" viewBox="0 0 318 66" aria-hidden="true">
    <defs>
      <linearGradient id="ctaFill" x1="0" y1="0" x2="0" y2="1">
        <stop offset="0%" stop-color="var(--red-light)"/>
        <stop offset="100%" stop-color="var(--red-deep)"/>
      </linearGradient>
    </defs>
    <path d="M0 0 H292 L316 33 L292 66 H0 Z" fill="url(#ctaFill)"/>
  </svg>
  <div class="cta__label">SHOP NOW</div>
</div>
</body>
</html>
```